M Website

We need a website design for a construction plant company. You may use a combination of our photos and the stock images. See the logo for company colours. It also be of great value to see moving pictures like the ones on the link: https://www.brakveldplant.co.za/about-us. See our uploaded files for content.

Target Market(s)

Construction

Number of Pages Required

5+ page

```html
<!DOCTYPE html>
<html lang="en">
<head>
<meta charset="utf-8">
<title>Brakveld — Logistics and Plant Hire</title>
<link href="https://fonts.googleapis.com/css2?family=Poppins:wght@300;400;500;600;700&display=swap" rel="stylesheet">
<style>
:root{
  --yellow:#f5c211;
  --dark:#1f1f1f;
  --ink:#2b2b2b;
  --muted:#777;
  --light:#f1f1f1;
  --brown:#6e4425;
  --footer:#2a2523;
  --white:#fff;
}
*{box-sizing:border-box;margin:0;padding:0}
html,body{width:1200px;height:4972px;overflow:hidden}
body{font-family:'Poppins',sans-serif;color:var(--ink);background:var(--white);position:relative}
.abs{position:absolute}
.btn{display:inline-flex;align-items:center;gap:10px;height:40px;padding:0 22px;font-size:11px;font-weight:600;letter-spacing:.5px;text-transform:uppercase;white-space:nowrap}
.btn-yellow{background:var(--yellow);color:var(--dark)}
.btn-dark{background:var(--dark);color:var(--white)}
.arrow{width:18px;height:8px}
.section-title{font-size:30px;font-weight:700;letter-spacing:1px;text-transform:uppercase;text-align:center}
.underline{width:60px;height:3px;background:var(--yellow);margin:10px auto 0}
.photo{position:absolute}
.dot{width:8px;height:8px;border-radius:50%;background:currentColor;display:inline-block}

.topbar{top:0;left:0;width:1200px;height:27px;background:#111;color:#ccc;font-size:11px;display:flex;align-items:center;justify-content:space-between;padding:0 150px}
.topbar .left{display:flex;gap:28px}
.topbar .social{display:flex;gap:14px;color:#ccc}
.hero{top:27px;left:0;width:1200px;height:620px;background:linear-gradient(180deg,#3a2a1a 0%,#8a5a2a 35%,#c58a3a 60%,#a06a30 100%)}
.hero::after{content:"";position:absolute;inset:0;background:linear-gradient(180deg,rgba(0,0,0,.55),rgba(0,0,0,.15) 40%,rgba(0,0,0,.05))}
.nav{top:27px;left:0;width:1200px;height:96px;display:flex;align-items:center;justify-content:space-between;padding:0 150px;z-index:2}
.brand{display:flex;align-items:center;gap:10px;color:var(--white);font-size:22px;font-weight:700}
.brand .mark{width:34px;height:34px;border-radius:50%;background:var(--yellow)}
.menu{display:flex;gap:34px;font-size:12px;color:var(--white);text-transform:uppercase}
.menu .active{color:var(--yellow);border-bottom:2px solid var(--yellow);padding-bottom:6px}
.hero-copy{top:245px;left:0;width:1200px;text-align:center;color:var(--white);z-index:2}
.hero-copy h1{font-size:46px;font-weight:500;line-height:1.05;text-transform:uppercase;letter-spacing:1px}
.hero-copy h1 b{color:var(--yellow);font-weight:700}
.hero-copy h1 strong{font-weight:700}
.hero-copy h1 em{font-style:normal;font-weight:400}
.hero-copy p{font-size:15px;margin-top:12px}
.hero-actions{top:428px;left:0;width:1200px;display:flex;justify-content:center;gap:14px;z-index:2}
.play{top:525px;left:960px;z-index:2;color:var(--white);font-size:13px;font-style:italic}
.play .ring{width:42px;height:42px;border:2px solid var(--white);border-radius:50%;display:flex;align-items:center;justify-content:center;margin-top:14px}

.quote{top:597px;left:149px;width:902px;height:98px;background:var(--white);box-shadow:0 8px 30px rgba(0,0,0,.15);display:flex;align-items:center;justify-content:space-between;padding:0 30px 0 36px;z-index:3}
.quote h2{font-size:28px;font-weight:700;display:flex;align-items:center;gap:18px}
.quote h2 span{font-weight:400}
.quote .btn{border:2px solid var(--dark);background:var(--white);color:var(--dark);padding:0 0 0 16px;height:44px}
.quote .btn i{display:flex;align-items:center;justify-content:center;background:var(--dark);width:44px;height:40px;margin-left:12px}

.who{top:840px;left:149px;width:420px}
.who h2{font-size:30px;font-weight:700;letter-spacing:1px}
.who .bar{width:50px;height:3px;background:var(--yellow);margin:8px 0 44px}
.who h4{font-size:11px;font-weight:500;text-transform:uppercase;line-height:1.7;color:#444}
.who p{font-size:11px;color:var(--muted);line-height:1.8;margin-top:22px}
.who .btn{margin-top:44px;height:36px}

.offering-band{top:1409px;left:0;width:1200px;height:482px;background:#222 linear-gradient(180deg,#1d1d1d,#2c2c2c)}
.offering-head{top:1495px;left:0;width:1200px;color:var(--white);text-align:center}
.offering-head p{font-size:12px;color:#ccc;width:560px;margin:26px auto 0;line-height:1.7}
.offer-card{top:1674px;left:149px;width:902px;height:448px;background:var(--white);box-shadow:0 10px 30px rgba(0,0,0,.12)}
.offer-item h3{font-size:16px;font-weight:600}
.offer-item ul{list-style:none;margin-top:16px;font-size:11px;color:var(--muted);line-height:2}
.offer-item li::before{content:"";display:inline-block;width:10px;height:2px;background:var(--yellow);margin-right:10px;vertical-align:middle}
.offer-item p{font-size:11px;color:var(--muted);line-height:1.8;margin-top:12px}

.usp-head{top:2240px;left:0;width:1200px}
.usp-head p{text-align:center;font-size:12px;color:var(--muted);margin-top:34px}
.usp{position:absolute;width:280px;text-align:center}
.usp svg{width:58px;height:58px;stroke:var(--ink);fill:none;stroke-width:2}
.usp h4{font-size:15px;font-weight:600;margin-top:22px}
.usp-active{top:2385px;left:460px;width:280px;height:265px;background:var(--dark);color:var(--white);box-shadow:0 12px 30px rgba(0,0,0,.3);padding-top:40px}
.usp-active svg{stroke:var(--yellow)}
.usp-active p{font-size:12px;color:#ddd;line-height:1.6;margin:8px 30px 0}

.testi{top:2917px;left:0;width:1200px;height:365px;background:var(--light)}
.bubble{top:2910px;left:210px}
.testi h2{position:absolute;top:120px;left:149px;font-size:22px;font-weight:700;line-height:1.1;text-transform:uppercase}
.testi h2 b{display:block;font-size:38px;letter-spacing:1px}
.testi .rule{position:absolute;top:228px;left:0;width:560px;height:1px;background:#ddd}
.testi blockquote{position:absolute;top:125px;left:590px;width:420px;font-size:12px;color:#555;font-style:italic;line-height:1.8}
.testi .qmark{position:absolute;top:100px;left:590px;font-size:40px;color:#bbb;line-height:1}
.testi cite{position:absolute;top:258px;left:590px;font-size:11px;font-weight:600;font-style:normal;letter-spacing:1px}
.avatars{position:absolute;top:268px;left:235px;display:flex;gap:8px;align-items:center}
.avatars span{width:40px;height:40px;border-radius:50%;background:linear-gradient(135deg,#c9c9c9,#9a9a9a)}

.team-head{top:3385px;left:0;width:1200px}
.team-head p{text-align:center;font-size:12px;color:var(--muted);margin-top:34px}
.member{position:absolute;top:3530px;width:260px;text-align:center}
.member .portrait{height:290px;background:linear-gradient(180deg,#ececec,#cfcfcf)}
.member h4{font-size:16px;font-weight:600;margin-top:30px}
.member h5{font-size:10px;color:var(--yellow);font-weight:600;letter-spacing:1px;text-transform:uppercase;margin-top:4px}
.member p{font-size:11px;color:var(--muted);line-height:1.7;margin:14px 20px 0}
.member .social{display:flex;justify-content:center;gap:14px;margin-top:16px;color:#888}
.member .social .dot{width:6px;height:6px}
.chev{top:3722px;width:14px;height:24px;stroke:#888;fill:none;stroke-width:2}

.contact-band{top:4227px;left:0;width:1200px;height:315px;background:linear-gradient(180deg,#74492a,#5c3a22)}
.contact{top:4111px;left:228px;width:744px;height:430px;background:var(--white);box-shadow:0 10px 40px rgba(0,0,0,.18);padding:55px 70px}
.contact h2{text-align:center;font-size:30px;font-weight:600}
.contact .sub{text-align:center;font-size:11px;color:var(--muted);margin-top:2px}
.form{display:grid;grid-template-columns:1fr 1fr;column-gap:40px;margin-top:40px}
.field{border-bottom:1px solid #ddd;font-size:11px;color:#999;padding:12px 0;margin-bottom:18px}
.contact .btn{display:flex;width:150px;margin:20px auto 0;height:38px;justify-content:center}

.footer{top:4541px;left:0;width:1200px;height:366px;background:var(--footer);color:#ccc}
.footer .brand{position:absolute;top:90px;left:175px}
.footer .news{position:absolute;top:225px;left:175px}
.footer h6{font-size:12px;font-weight:600;color:var(--white);text-transform:uppercase;letter-spacing:1px}
.footer .news .input{width:230px;border-bottom:1px solid #666;font-size:11px;color:#999;padding:12px 0;margin-top:8px;display:flex;justify-content:space-between}
.fcol{position:absolute;top:80px;font-size:11px;line-height:1.8}
.fcol h6{margin-bottom:12px}
.fcol .label{color:var(--yellow);font-weight:600}
.fcol .meta{margin-top:16px;color:var(--yellow)}
.bottombar{top:4907px;left:0;width:1200px;height:65px;background:#141414;color:#aaa;font-size:11px;display:flex;align-items:center;justify-content:space-between;padding:0 175px}
.bottombar .social{display:flex;gap:14px;align-items:center}
</style>
</head>
<body>

<div class="abs hero" role="img" aria-label="Construction machine excavating earth on a site at dusk"></div>
<div class="abs topbar">
  <div class="left"><span>info@brakveldplant.co.za</span><span>+27 (0)11 555 0142</span></div>
  <div class="social"><span class="dot"></span><span class="dot"></span><span class="dot"></span><span class="dot"></span></div>
</div>
<div class="abs nav">
  <div class="brand"><span class="mark"></span>Brakveld</div>
  <nav class="menu"><span class="active">Home</span><span>About Us</span><span>Our Mission</span><span>Projects</span><span>Certification</span><span>Contact</span></nav>
</div>
<div class="abs hero-copy">
  <h1>Transforming <b>Our Clients</b><br><strong>Vision Into</strong> <em>Reality</em></h1>
  <p>Lorem Ipsum is simply dummy text of the printing and typesetting industry.</p>
</div>
<div class="abs hero-actions">
  <span class="btn btn-yellow">Read More <svg class="arrow" viewBox="0 0 18 8"><path d="M0 4h16M13 1l3 3-3 3" stroke="#1f1f1f" fill="none" stroke-width="1.5"/></svg></span>
  <span class="btn btn-dark">View Project <svg class="arrow" viewBox="0 0 18 8"><path d="M0 4h16M13 1l3 3-3 3" stroke="#fff" fill="none" stroke-width="1.5"/></svg></span>
</div>
<div class="abs play">
  <span style="margin-left:40px">Play Video</span>
  <div class="ring"><svg width="12" height="14" viewBox="0 0 12 14"><path d="M1 1l10 6-10 6z" fill="#fff"/></svg></div>
</div>

<div class="abs quote">
  <h2><svg width="60" height="16" viewBox="0 0 60 16"><g stroke="#f5c211" stroke-width="4"><path d="M2 16L10 0M14 16L22 0M26 16L34 0M38 16L46 0M50 16L58 0"/></g></svg>Get a Quote <span>For Your Project</span></h2>
  <span class="btn">Free Quote <i><svg class="arrow" viewBox="0 0 18 8"><path d="M0 4h16M13 1l3 3-3 3" stroke="#fff" fill="none" stroke-width="1.5"/></svg></i></span>
</div>

<section class="abs who">
  <h2>WHO WE ARE?</h2>
  <div class="bar"></div>
  <h4>Delivering high quality multidisciplinary engineering and construction projects</h4>
  <p>Brakveld Logistics and Plant Hire (Pty) Ltd is a Black Owned Construction and Plant Hire company operating mainly from the head office in Midrand, Gauteng. The company was established in 2014 and has worked in various municipal jurisdictions within South Africa.</p>
  <span class="btn btn-yellow">Read More <svg class="arrow" viewBox="0 0 18 8"><path d="M0 4h16M13 1l3 3-3 3" stroke="#1f1f1f" fill="none" stroke-width="1.5"/></svg></span>
</section>
<div class="photo" style="top:800px;left:680px;width:175px;height:180px;background:linear-gradient(135deg,#d9a52a,#5c4a2c)" role="img" aria-label="Yellow backhoe loader on site"></div>
<div class="photo" style="top:995px;left:680px;width:175px;height:180px;background:linear-gradient(135deg,#7b6a4a,#3f3a30)" role="img" aria-label="Workers in safety gear at a trench"></div>
<div class="photo" style="top:900px;left:870px;width:180px;height:180px;background:linear-gradient(180deg,#5a7a4a,#3a3a3a)" role="img" aria-label="Freshly laid asphalt road"></div>
<div class="photo" style="top:1095px;left:870px;width:180px;height:180px;background:linear-gradient(180deg,#8aa0b8,#4a4a46)" role="img" aria-label="Paving machine laying asphalt"></div>

<div class="abs offering-band"></div>
<div class="abs offering-head">
  <h2 class="section-title">Our Offering</h2>
  <div class="underline"></div>
  <p>Brakveld Logistics and Plant Hire (Pty) Ltd has expertise in the following key fields and has successfully executed projects in most of them.</p>
</div>
<div class="abs offer-card">
  <div class="photo" style="top:26px;left:26px;width:150px;height:150px;background:linear-gradient(180deg,#8ab0d0,#4a4a4a)" role="img" aria-label="Road construction with asphalt"></div>
  <div class="abs offer-item" style="top:36px;left:196px;width:230px">
    <h3>Roads &amp; Stormwater</h3>
    <ul><li>Road upgrades and rehabilitation</li><li>Construction of new paved roads – paving blocks and asphalt roads</li></ul>
  </div>
  <div class="photo" style="top:26px;left:466px;width:410px;height:170px;background:linear-gradient(135deg,#d97a2a,#4a6a8a)" role="img" aria-label="Workers in orange overalls next to a truck"></div>
  <div class="photo" style="top:228px;left:26px;width:150px;height:150px;background:linear-gradient(180deg,#b88a55,#6a4a2a)" role="img" aria-label="Water pipe laid in a trench"></div>
  <div class="abs offer-item" style="top:240px;left:196px;width:230px">
    <h3>Water</h3>
    <ul><li>Grey water reticulation</li><li>Potable water reticulation</li></ul>
  </div>
  <div class="abs offer-item" style="top:212px;left:466px;width:410px">
    <h3>Sanitation</h3>
    <ul><li>Grey water reticulation</li></ul>
    <p>The projects descriptions are provided in the "Record of Experience" although the head office is in Midrand, Johannesburg. Brakveld has successfully completed projects in the following regions.</p>
  </div>
  <span class="abs btn btn-yellow" style="top:388px;left:690px;height:36px;font-size:10px">Read More Offering <svg class="arrow" viewBox="0 0 18 8"><path d="M0 4h16M13 1l3 3-3 3" stroke="#1f1f1f" fill="none" stroke-width="1.5"/></svg></span>
</div>

<div class="abs usp-head">
  <h2 class="section-title">Our USP</h2>
  <div class="underline"></div>
  <p>We are committed to achieving this through the following:</p>
</div>
<div class="usp" style="top:2430px;left:150px">
  <svg viewBox="0 0 58 58"><circle cx="22" cy="18" r="8"/><path d="M8 50c0-12 6-18 14-18s14 6 14 18"/><path d="M36 26h14v12H36z"/></svg>
  <h4>Integrity</h4>
</div>
<div class="abs usp usp-active">
  <svg viewBox="0 0 58 58"><rect x="10" y="8" width="38" height="44" rx="3"/><circle cx="29" cy="28" r="9"/><path d="M25 28l3 3 6-6M18 8v-4h22v4"/></svg>
  <h4>Accountability</h4>
  <p>Providing a services to our Clients which meets their expectations.</p>
</div>
<div class="usp" style="top:2430px;left:770px">
  <svg viewBox="0 0 58 58"><path d="M29 6L52 50H6z"/><path d="M29 20L42 44H16z"/></svg>
  <h4>Reliability</h4>
</div>
<div class="usp" style="top:2675px;left:150px">
  <svg viewBox="0 0 58 58"><path d="M8 50h42M14 50V38M24 50V30M34 50V22M44 50V14M12 30L40 10M34 10h6v6"/></svg>
  <h4>Capability</h4>
</div>
<div class="usp" style="top:2675px;left:460px">
  <svg viewBox="0 0 58 58"><circle cx="29" cy="29" r="8"/><circle cx="29" cy="8" r="4"/><circle cx="50" cy="29" r="4"/><circle cx="29" cy="50" r="4"/><circle cx="8" cy="29" r="4"/><path d="M29 12v9M46 29h-9M29 46v-9M12 29h9"/></svg>
  <h4>Adaptability</h4>
</div>
<div class="usp" style="top:2675px;left:770px">
  <svg viewBox="0 0 58 58"><rect x="12" y="6" width="30" height="40"/><path d="M18 16h18M18 24h18M18 32h10"/><circle cx="42" cy="44" r="7"/><path d="M38 50l-2 6 6-3 6 3-2-6"/></svg>
  <h4>Ethics</h4>
</div>

<section class="abs testi">
  <h2>What Our<b>Customer Says</b></h2>
  <div class="rule"></div>
  <span class="qmark">“</span>
  <blockquote>Lorem Ipsum is simply dummy text of the printing and typesetting industry. Lorem Ipsum has been the industry's standard dummy text ever since the 1500s, when an unknown printer took a galley of type.</blockquote>
  <cite>MARLA KESWICK</cite>
  <div class="avatars">
    <span></span><span></span><span></span><span></span>
    <svg width="30" height="12" viewBox="0 0 30 12" style="margin-left:8px"><path d="M6 1L1 6l5 5M24 1l5 5-5 5" stroke="#555" fill="none" stroke-width="1.5"/></svg>
  </div>
</section>
<svg class="abs bubble" width="90" height="60" viewBox="0 0 90 60"><path d="M0 0h90v30c0 12-20 22-45 22L30 60l2-9C12 48 0 40 0 30z" fill="#f5c211"/></svg>

<div class="abs team-head">
  <h2 class="section-title">Innovative Team</h2>
  <div class="underline"></div>
  <p>Lorem Ipsum is simply dummy text of the printing and typesetting industry. Lorem Ipsum has been the industry.</p>
</div>
<svg class="abs chev" style="left:130px" viewBox="0 0 14 24"><path d="M12 2L2 12l10 10"/></svg>
<svg class="abs chev" style="left:1050px" viewBox="0 0 14 24"><path d="M2 2l10 10-10 10"/></svg>
<div class="member" style="left:165px">
  <div class="portrait" role="img" aria-label="Portrait of team member in grey t-shirt"></div>
  <h4>Daniel Roos</h4><h5>Managing Director</h5>
  <p>The Managing Director is responsible for ensuring that the strategy and organisation of the company is sound.</p>
  <div class="social"><span class="dot"></span><span class="dot"></span><span class="dot"></span></div>
</div>
<div class="member" style="left:470px">
  <div class="portrait" role="img" aria-label="Portrait of team member in suit"></div>
  <h4>Julian Whitfield</h4><h5>Contracts Director</h5>
  <p>The Contracts Director will attend to undertake a quotation task whenever required to supplement.</p>
  <div class="social"><span class="dot"></span><span class="dot"></span><span class="dot"></span></div>
</div>
<div class="member" style="left:775px">
  <div class="portrait" role="img" aria-label="Portrait of team member in shirt"></div>
  <h4>Owen Marais</h4><h5>Estimator</h5>
  <p>The Estimator is responsible for all tenders that is submitted by Brakveld Logistics.</p>
  <div class="social"><span class="dot"></span><span class="dot"></span><span class="dot"></span></div>
</div>

<div class="abs contact-band" role="img" aria-label="Brown earthworks background"></div>
<section class="abs contact">
  <h2>Get in touch</h2>
  <p class="sub">Any questions or remarks? Just write us a message!</p>
  <div class="form">
    <div><div class="field">Name</div><div class="field">Email Address</div><div class="field">Phone</div></div>
    <div><div class="field">Message</div><div class="field">&nbsp;</div><div class="field">&nbsp;</div></div>
  </div>
  <span class="btn btn-yellow">Submit Now <svg class="arrow" viewBox="0 0 18 8"><path d="M0 4h16M13 1l3 3-3 3" stroke="#1f1f1f" fill="none" stroke-width="1.5"/></svg></span>
</section>

<footer class="abs footer">
  <div class="brand"><span class="mark"></span>Brakveld</div>
  <div class="news">
    <h6>Newsletter</h6>
    <div class="input"><span>Enter your email address</span><svg width="16" height="14" viewBox="0 0 16 14"><path d="M1 7l14-6-4 12-3-5z" stroke="#ccc" fill="none"/></svg></div>
  </div>
  <div class="fcol" style="left:475px">
    <h6>Company</h6>
    Home<br>About Us<br>Our Mission<br>Projects<br>Certification<br>Contact
  </div>
  <div class="fcol" style="left:635px;width:220px">
    <h6>Address</h6>
    <span class="label">Head Office</span><br>Unit 12, Kestrel Park<br>18 Lorimer Road, Midrand<br>Gauteng, 1685
    <div class="meta">+27 (0)11 555 0142</div>
  </div>
  <div class="fcol" style="left:890px;width:200px">
    <h6>&nbsp;</h6>
    <span class="label">Free State Office</span><br>Unit 4, Ridgeway Centre<br>Bloemfontein, 9301
    <div class="meta">info@brakveldplant.co.za</div>
  </div>
</footer>
<div class="abs bottombar">
  <span>© 2019 Brakveld Plant Hire. All rights reserved.</span>
  <div class="social">FOLLOW US ON: <span class="dot"></span><span class="dot"></span><span class="dot"></span><span class="dot"></span></div>
</div>

</body>
</html>
```